Flyer Design job - Occupational Therapy Flyer!

We are looking for a flyer design.
SPECIFICATIONS:
Size: 8 1/2 x 11, bleeds .125 inches all around.
CMYK colors only. One sided print.

THE COMPANY:
The clientele is an all boys school.
- We do not want any photos of kids, or people.
- Attached is the image we want to use, along with their logo and copy.

Here is the copy as well: Copy for flyer:
The Birchfield Academy is excited to welcome (This is the name of the boys school that will not have occupational services offered in their school).
Little Sprout Therapy (logo)
We’re proud to provide your child with professional occupational therapy services right in his school. The familiar environment paired with our expert and caring therapists will give your son the chance to grow and thrive without leaving his comfort zone.
• Mrs. Miriam Feldstone, OTR/L, Director of Occupational Therapy Services Working in private practice for over 19 years
• Fully equipped therapy gym
• No transportation necessary (no missing Yeshiva or work)
• Introductory low rates for evaluations and therapy sessions
• Communication and collaboration with the parents, Principals, Rebbeim, teachers, and other therapists
• Therapy is exclusive to The Birchfield Academy, servicing boys from primary through eighth grade.

(Highlighted text:) Private therapy in a school setting

Call or email now to schedule your evaluation
555-284-1937 littlesprouttherapy1@examplemail.com
Little Sprout Therapy • PO Box 912 • Fairhollow ST 00000

Target Market(s)

Parent of school aged boys. (preschool - 8th grade).

Colors

Designer to choose colors to be used in the design.

Requirements
Must have
• My logo, copy, the image i supplied. It should be well laid out, with nice typography, easy to read, and look fun.
• It must be able to be saved down to CS6. Adobe suite.
• CMYK
Should not have
• It should not look "girly".
• No images of people or kids.

```html
<!DOCTYPE html>
<html lang="en">
<head>
<meta charset="utf-8">
<title>Little Sprout Therapy – Birchfield Academy Flyer</title>
<link href="https://fonts.googleapis.com/css2?family=Bebas+Neue&family=Lato:wght@400;900&display=swap" rel="stylesheet">
<style>
  :root {
    --yellow: #ffc20e;
    --teal: #0aa3a1;
    --magenta: #e5157a;
    --lime: #c4d82e;
    --ink: #1d1d1d;
    --text: #333333;
    --white: #ffffff;
    --stage: #8c8c8c;
  }
  html, body { margin: 0; padding: 0; overflow: hidden; }
  body {
    width: 1200px; height: 1200px;
    background: var(--stage);
    position: relative;
    font-family: "Lato", sans-serif;
  }
  .flyer {
    position: absolute; left: 175px; top: 50px;
    width: 850px; height: 1100px;
    background: var(--white);
    overflow: hidden;
    box-shadow: 0 8px 30px rgba(0,0,0,.35);
  }
  .flyer-shapes { position: absolute; inset: 0; }
  .hero-photo-ring {
    position: absolute; left: 15px; top: 27px;
    width: 550px; height: 550px; border-radius: 50%;
    background: var(--white);
    box-shadow: 4px 4px 0 var(--ink);
  }
  .hero-photo {
    position: absolute; left: 13px; top: 13px;
    width: 524px; height: 524px; border-radius: 50%;
    background: linear-gradient(180deg, #c9cdd8 0%, #b7b9c4 38%, #3a4fb8 58%, #2b3ea6 100%);
  }
  .headline {
    position: absolute; right: 16px; top: 312px;
    margin: 0; text-align: right;
    font-family: "Bebas Neue", sans-serif; font-weight: 400;
    font-size: 47px; line-height: 49px; letter-spacing: -0.5px;
    text-shadow: 3px 3px 0 var(--ink);
  }
  .headline span { display: block; }
  .headline .teal { color: var(--teal); }
  .headline .yellow { color: var(--yellow); }
  .headline .magenta { color: var(--magenta); }
  .headline-rule {
    position: absolute; left: 627px; top: 529px;
    width: 207px; height: 5px; background: var(--lime);
  }
  .benefits {
    position: absolute; left: 512px; top: 566px; width: 322px;
    margin: 0; padding: 0; list-style: none;
    font-size: 15.5px; line-height: 20px; color: var(--text);
  }
  .benefits li { position: relative; margin-bottom: 8px; text-align: justify; }
  .benefits li::before {
    content: ""; position: absolute; left: -14px; top: 5px;
    width: 8px; height: 8px; transform: rotate(45deg);
  }
  .benefits li:nth-child(3n+1)::before { background: var(--magenta); }
  .benefits li:nth-child(3n+2)::before { background: #f5a623; }
  .benefits li:nth-child(3n)::before { background: var(--teal); }
  .brand {
    position: absolute; left: 16px; top: 604px;
    display: flex; align-items: center; gap: 12px;
  }
  .brand-dot { width: 34px; height: 34px; border-radius: 50%; background: var(--yellow); }
  .brand-name { font-weight: 900; font-size: 47px; line-height: 60px; color: var(--teal); letter-spacing: -0.5px; }
  .intro {
    position: absolute; left: 16px; top: 703px; width: 456px;
    margin: 0; font-size: 21.5px; line-height: 27px;
    color: var(--text); text-align: justify;
  }
  .tagline {
    position: absolute; left: 16px; top: 887px;
    width: 456px; height: 90px; border-radius: 10px;
    background: var(--magenta);
    box-shadow: 4px 4px 0 var(--ink);
    display: flex; align-items: center; justify-content: center;
    font-family: "Bebas Neue", sans-serif; font-size: 32px;
    color: var(--yellow); letter-spacing: 0.3px;
  }
  .address {
    position: absolute; left: 16px; top: 1005px;
    display: flex; align-items: center; gap: 18px;
  }
  .address-icon { width: 62px; height: 62px; }
  .address-text {
    font-family: "Bebas Neue", sans-serif; color: var(--yellow);
    font-size: 30px; line-height: 31px;
  }
  .contact {
    position: absolute; left: 505px; top: 990px; width: 330px;
    text-align: center; color: var(--white);
  }
  .contact-cta { font-family: "Bebas Neue", sans-serif; font-size: 19px; line-height: 20px; }
  .contact-phone { font-weight: 900; font-size: 46px; line-height: 50px; letter-spacing: 0.5px; }
  .contact-email {
    margin-top: 4px; height: 27px; border-radius: 14px;
    background: var(--lime); font-size: 14.5px; line-height: 27px;
  }
</style>
</head>
<body>
  <main class="flyer">
    <svg class="flyer-shapes" viewBox="0 0 850 1100" width="850" height="1100" aria-hidden="true">
      <path fill="var(--yellow)" d="M0 0 H850 V225 C820,215 795,170 765,195 C735,160 688,185 680,235 C640,228 618,268 640,300 C600,302 582,340 602,372 L560,560 C480,600 400,620 360,612 C300,642 200,600 150,622 C100,592 40,602 0,604 Z"/>
      <path fill="var(--teal)" d="M409 1100 C412 1050 450 1030 480 1035 C490 985 530 965 570 975 C600 925 680 915 720 945 C750 905 820 895 850 905 V1100 Z"/>
    </svg>

    <div class="hero-photo-ring">
      <div class="hero-photo" role="img" aria-label="Photograph of a sensory therapy gym with a hanging tire swing, a trapeze bar, padded blue mats and foam steps"></div>
    </div>

    <h1 class="headline">
      <span class="teal">The Birchfield</span>
      <span class="teal">Academy</span>
      <span class="yellow">Is excited to</span>
      <span class="magenta">Welcome</span>
    </h1>
    <div class="headline-rule"></div>

    <ul class="benefits">
      <li>Mrs. Miriam Feldstone, OTR/L, Director of Occupational Therapy Services Working in private practice for over 19 years</li>
      <li>Fully equipped therapy gym</li>
      <li>No transportation necessary (no missing Yeshiva or work)</li>
      <li>Introductory low rates for evaluations and therapy sessions</li>
      <li>Communication and collaboration with the parents, Principals, Rebbeim, teachers, and other therapists</li>
      <li>Therapy is exclusive to the Birchfield Academy, servicing boys from primary through eighth grade.</li>
    </ul>

    <div class="brand">
      <span class="brand-dot"></span>
      <span class="brand-name">Little Sprout Therapy</span>
    </div>

    <p class="intro">We’re proud to provide your child with professional occupational therapy services right in his school. The familiar environment paired with our expert and caring therapists will give your son the chance to grow and thrive without leaving his comfort zone.</p>

    <div class="tagline">Private therapy in a school setting</div>

    <div class="address">
      <svg class="address-icon" viewBox="0 0 62 62" aria-hidden="true">
        <path fill="var(--teal)" stroke="var(--ink)" stroke-width="2" d="M31 4 L59 30 H51 V58 H37 V42 H25 V58 H11 V30 H3 Z"/>
      </svg>
      <div class="address-text">
        <div>Little Sprout Therapy</div>
        <div>PO Box 912, Fairhollow ST 00000</div>
      </div>
    </div>

    <div class="contact">
      <div class="contact-cta">Call or email now to schedule your evaluation</div>
      <div class="contact-phone">555-284-1937</div>
      <div class="contact-email">littlesprouttherapy1@examplemail.com</div>
    </div>
  </main>
</body>
</html>
```